Business card for a boutique travel agency VELIRANDE

we need a business card design - double sided. We would like to have a very elegant, sophisticated but modern design. we are travel consultants and our business focus is Europe, mainly the city of Paris. We would like to receive designs in white and silver, black color but if you are confident that we should pick up a color to make it different and more beautful...go ahead! We are going to give business cards to our clients and business partners. It is important to be perceived as elegant, modern and trustful. Please check jpg references.

Target Market(s)

Velirande primary clients are individuals, couples and affinity groups of high-net-worth who travel for leisure at least once per year. Seeking the ultimate travel experience, the target clients demand the finest quality activities and accommodations accompanied by a superior level of service.

Industry/Entity Type

Travel Industry

Contact Information for Business Card

Liliana Quesada
- liliana@velirande-mail.example
- +55 11 98437.5216
- velirande-mail.example
- unique travel experiences (we would like to see this signature printed as a detail)

Font styles to use
Sans Serif

Colors

Designer to choose colors to be used in the design.

Requirements
Must have
• the Velirande logo that I have attached
Nice to have
• we would like to have some nice detail, something different that shows that we care about,... we are detail oriented.
Should not have
• decorative fonts

```html
<!DOCTYPE html>
<html lang="en">
<head>
<meta charset="utf-8">
<title>Velirande — Business Card</title>
<link href="https://fonts.googleapis.com/css2?family=Josefin+Sans:wght@300;400&display=swap" rel="stylesheet">
<style>
  :root {
    --backdrop: #3b3b3c;
    --card: #1b1b1c;
    --card-edge: #262627;
    --ink: #f2f2f2;
    --ink-soft: #d9d9d9;
    --ring: #2c2c2e;
    --ring-light: #3a3a3d;
  }
  * { margin: 0; padding: 0; box-sizing: border-box; }
  html, body {
    width: 799px;
    height: 1200px;
    overflow: hidden;
    background: var(--backdrop);
    font-family: "Josefin Sans", sans-serif;
  }
  .sheet {
    position: relative;
    width: 799px;
    height: 1200px;
  }
  .card {
    position: absolute;
    left: 80px;
    width: 640px;
    height: 366px;
    background: var(--card);
    border: 1px solid var(--card-edge);
    border-radius: 4px;
    box-shadow: 0 12px 30px rgba(0,0,0,0.35);
    overflow: hidden;
  }
  .card--front { top: 117px; }
  .card--back { top: 717px; }

  .emblem-ring {
    position: absolute;
    border-radius: 50%;
  }
  .card--front .emblem-ring {
    width: 190px;
    height: 190px;
    left: 245px;
    top: 88px;
    border: 14px solid var(--ring);
  }
  .card--back .emblem-ring {
    width: 250px;
    height: 250px;
    left: 400px;
    top: 150px;
    border: 18px solid var(--ring-light);
    background: var(--card);
  }

  .wordmark {
    position: absolute;
    color: var(--ink);
    font-weight: 300;
    text-transform: uppercase;
    white-space: nowrap;
  }
  .card--front .wordmark {
    left: 0;
    width: 100%;
    top: 160px;
    text-align: center;
    font-size: 38px;
    letter-spacing: 0.42em;
    padding-left: 0.42em;
  }
  .card--back .wordmark {
    left: 44px;
    top: 46px;
    font-size: 24px;
    letter-spacing: 0.42em;
  }

  .holder {
    position: absolute;
    left: 44px;
    top: 164px;
    color: var(--ink);
  }
  .holder-name {
    font-size: 19px;
    font-weight: 300;
    letter-spacing: 0.06em;
    text-transform: uppercase;
    margin-bottom: 18px;
  }
  .holder-contact {
    list-style: none;
    color: var(--ink-soft);
    font-size: 13px;
    font-weight: 300;
    line-height: 1.55;
    letter-spacing: 0.01em;
  }
</style>
</head>
<body>
<main class="sheet">
  <section class="card card--front" aria-label="Card front">
    <div class="emblem-ring" aria-hidden="true"></div>
    <h1 class="wordmark">Velirande</h1>
  </section>

  <section class="card card--back" aria-label="Card back">
    <div class="emblem-ring" aria-hidden="true"></div>
    <p class="wordmark">Velirande</p>
    <div class="holder">
      <p class="holder-name">Liliana Quesada</p>
      <ul class="holder-contact">
        <li>+55 11 98437.5216</li>
        <li>liliana@velirande-mail.example</li>
        <li>www.velirande-mail.example</li>
      </ul>
    </div>
  </section>
</main>
</body>
</html>
```